Step and Repeat Backdrop for wedding reception photo booth

Would like to have a Step and Repeat Backdrop (8 foot high by 10 foot wide) that incorporates the wedding logo (attached) and the names Elena and Gavin. Background should be white, and wedding colors are burgundy and gold. Show me creativity :-) I have included some random samples.

```html
<!DOCTYPE html>
<html lang="en">
<head>
<meta charset="utf-8">
<title>Elena &amp; Gavin — Step and Repeat Backdrop</title>
<link rel="stylesheet" href="https://fonts.googleapis.com/css2?family=Cormorant+Garamond:wght@500&display=swap">
<style>
  :root {
    --stage: #e6e6e6;
    --banner: #ffffff;
    --gold: #b08d3c;
  }
  * { box-sizing: border-box; margin: 0; padding: 0; }
  html, body {
    width: 1200px;
    height: 764px;
    overflow: hidden;
    background: var(--stage);
  }
  .canvas {
    position: relative;
    width: 1200px;
    height: 764px;
    background: radial-gradient(ellipse at center, #f4f4f4 0%, var(--stage) 75%);
  }
  .backdrop {
    position: absolute;
    left: 136px;
    top: 12px;
    width: 928px;
    height: 740px;
    background: var(--banner);
    padding: 16px 0 0 31px;
    display: grid;
    grid-template-columns: repeat(4, 218px);
    grid-template-rows: repeat(7, 101px);
  }
  .repeat-unit {
    display: flex;
    align-items: center;
  }
  .monogram-mark {
    flex: 0 0 auto;
    width: 60px;
    height: 60px;
    margin: 0 20px 0 7px;
    border-radius: 50%;
    background: var(--gold);
  }
  .couple-names {
    font-family: "Cormorant Garamond", Georgia, serif;
    font-weight: 500;
    font-size: 22px;
    color: var(--gold);
    white-space: nowrap;
    letter-spacing: 0.2px;
  }
</style>
</head>
<body>
<main class="canvas">
  <section class="backdrop" aria-label="Step and repeat backdrop">
    <div class="repeat-unit"><span class="monogram-mark"></span><span class="couple-names">Elena &amp; Gavin</span></div>
    <div class="repeat-unit"><span class="monogram-mark"></span><span class="couple-names">Elena &amp; Gavin</span></div>
    <div class="repeat-unit"><span class="monogram-mark"></span><span class="couple-names">Elena &amp; Gavin</span></div>
    <div class="repeat-unit"><span class="monogram-mark"></span><span class="couple-names">Elena &amp; Gavin</span></div>

    <div class="repeat-unit"><span class="monogram-mark"></span><span class="couple-names">Elena &amp; Gavin</span></div>
    <div class="repeat-unit"><span class="monogram-mark"></span><span class="couple-names">Elena &amp; Gavin</span></div>
    <div class="repeat-unit"><span class="monogram-mark"></span><span class="couple-names">Elena &amp; Gavin</span></div>
    <div class="repeat-unit"><span class="monogram-mark"></span><span class="couple-names">Elena &amp; Gavin</span></div>

    <div class="repeat-unit"><span class="monogram-mark"></span><span class="couple-names">Elena &amp; Gavin</span></div>
    <div class="repeat-unit"><span class="monogram-mark"></span><span class="couple-names">Elena &amp; Gavin</span></div>
    <div class="repeat-unit"><span class="monogram-mark"></span><span class="couple-names">Elena &amp; Gavin</span></div>
    <div class="repeat-unit"><span class="monogram-mark"></span><span class="couple-names">Elena &amp; Gavin</span></div>

    <div class="repeat-unit"><span class="monogram-mark"></span><span class="couple-names">Elena &amp; Gavin</span></div>
    <div class="repeat-unit"><span class="monogram-mark"></span><span class="couple-names">Elena &amp; Gavin</span></div>
    <div class="repeat-unit"><span class="monogram-mark"></span><span class="couple-names">Elena &amp; Gavin</span></div>
    <div class="repeat-unit"><span class="monogram-mark"></span><span class="couple-names">Elena &amp; Gavin</span></div>

    <div class="repeat-unit"><span class="monogram-mark"></span><span class="couple-names">Elena &amp; Gavin</span></div>
    <div class="repeat-unit"><span class="monogram-mark"></span><span class="couple-names">Elena &amp; Gavin</span></div>
    <div class="repeat-unit"><span class="monogram-mark"></span><span class="couple-names">Elena &amp; Gavin</span></div>
    <div class="repeat-unit"><span class="monogram-mark"></span><span class="couple-names">Elena &amp; Gavin</span></div>

    <div class="repeat-unit"><span class="monogram-mark"></span><span class="couple-names">Elena &amp; Gavin</span></div>
    <div class="repeat-unit"><span class="monogram-mark"></span><span class="couple-names">Elena &amp; Gavin</span></div>
    <div class="repeat-unit"><span class="monogram-mark"></span><span class="couple-names">Elena &amp; Gavin</span></div>
    <div class="repeat-unit"><span class="monogram-mark"></span><span class="couple-names">Elena &amp; Gavin</span></div>

    <div class="repeat-unit"><span class="monogram-mark"></span><span class="couple-names">Elena &amp; Gavin</span></div>
    <div class="repeat-unit"><span class="monogram-mark"></span><span class="couple-names">Elena &amp; Gavin</span></div>
    <div class="repeat-unit"><span class="monogram-mark"></span><span class="couple-names">Elena &amp; Gavin</span></div>
    <div class="repeat-unit"><span class="monogram-mark"></span><span class="couple-names">Elena &amp; Gavin</span></div>
  </section>
</main>
</body>
</html>
```